New funky, super creative logo design for printing business

Stamp, Wrap and Ship

We are a new digital printing business, based on the Gold Coast of Australia. We have a web site under construction - www.stampwrapandship.net, which will aim at the Business to Business market. We are digital printers, offering a wide variety of print products from business cards to wide format print jobs for consumers and small to medium sized business'. We offer up to date technological, digital and wide format print, at hi octane speed. Our prices are very competitive, and turnaround is super fast.

We like to think outside the box, and this should shine through in the design and colours that you use. Be bold and creative, we want to stand out from the crowd.

We will also soon be needing a full suite of marketing collaterals - posters, letterheads, scrap pads, calendars, banners etc. but this will come later, once we have decided on the logo and layouts.

We want a vibrant, bold image, communicating vibrancy and excitement.

Details on the card are company name: Stamp, Wrap and Ship.
www.stampwrapandship.net.
contact: Corinne (+61)437182265
e-mail:corinne@stampwrapandship.net

I must be able to change some of the details such as the name and number on the card.

Target Market(s)

Business to business, small retail, some individuals

Industry/Entity Type

Construction

Requirements
Must have
• Unique funky logo.
Nice to have
• A three dimensional look,with depth in the logo.

```html
<!DOCTYPE html>
<html lang="en">
<head>
<meta charset="utf-8">
<title>Stamp, Wrap &amp; Ship – Folded Card</title>
<link href="https://fonts.googleapis.com/css2?family=Arimo:wght@400;700&display=swap" rel="stylesheet">
<style>
  :root {
    --backdrop: #f1f1f1;
    --card: #ffffff;
    --pocket-light: #f7f7f7;
    --pocket-dark: #d2d2d2;
    --brand-green: #00ff00;
    --ink: #111111;
    --rule: #e3e3e3;
    --dim-line: #7a7a7a;
  }
  * { margin: 0; padding: 0; box-sizing: border-box; }
  html, body { width: 1200px; height: 796px; overflow: hidden; }
  body {
    position: relative;
    background: radial-gradient(ellipse at 50% 45%, #fafafa 0%, var(--backdrop) 70%);
    font-family: "Arimo", Arial, sans-serif;
    color: var(--ink);
  }
  .view-label {
    position: absolute;
    font-size: 17px;
  }
  .view-label--folded { left: 213px; top: 192px; }
  .view-label--open { left: 605px; top: 61px; }

  /* Folded view */
  .folded-card {
    position: absolute;
    left: 210px; top: 234px;
    width: 290px; height: 292px;
    background: radial-gradient(ellipse at 50% 62%, var(--pocket-light) 0%, #ececec 55%, var(--pocket-dark) 100%);
    overflow: hidden;
  }
  .folded-card__flap {
    position: absolute;
    left: 4px; top: 0;
    width: 282px; height: 57px;
    background: linear-gradient(#ffffff, #ececec);
    border-radius: 0 0 34px 34px;
    box-shadow: 0 4px 8px rgba(0,0,0,0.12);
  }
  .folded-card__mark {
    position: absolute;
    left: 70px; top: 33px;
    width: 152px; height: 150px;
    background: var(--brand-green);
    display: flex; align-items: center; justify-content: center;
  }
  .folded-card__mark::before {
    content: "";
    position: absolute; left: 0; right: 0; top: 24px;
    border-top: 1px solid rgba(0,0,0,0.25);
  }

  .brand-name {
    font-weight: 700;
    text-transform: uppercase;
    text-align: left;
    line-height: 0.95;
    color: var(--ink);
  }
  .folded-card__mark .brand-name { font-size: 22px; }

  /* Open view */
  .open-card {
    position: absolute;
    left: 602px; top: 99px;
    width: 291px; height: 623px;
    background: var(--card);
    border-radius: 20px 20px 0 0;
    box-shadow: 0 2px 10px rgba(0,0,0,0.08);
  }
  .open-card__fold {
    position: absolute; left: 0; right: 0;
    border-top: 1px solid var(--rule);
  }
  .open-card__fold--top { top: 37px; }
  .open-card__fold--middle { top: 331px; }
  .open-card__mark {
    position: absolute;
    left: 19px; top: 56px;
    width: 256px; height: 252px;
    background: var(--brand-green);
    display: flex; align-items: center; justify-content: center;
  }
  .open-card__mark .brand-name { font-size: 38px; }

  .contact {
    position: absolute;
    left: 22px; top: 466px;
    font-size: 16px;
  }
  .contact__company { font-size: 19px; font-weight: 700; margin-bottom: 12px; }
  .contact__line { line-height: 26px; }
  .contact__web { margin-top: 24px; }

  /* Dimensions */
  .dimensions { position: absolute; left: 0; top: 0; }
  .dim-label {
    position: absolute;
    font-size: 14px;
  }
  .dim-label--vertical { writing-mode: vertical-rl; }
  .dim-label--folded-height { left: 525px; top: 362px; }
  .dim-label--folded-width { left: 337px; top: 551px; }
  .dim-label--open-height { left: 948px; top: 425px; }
  .dim-label--flap-height { left: 916px; top: 558px; }
</style>
</head>
<body>
  <svg class="dimensions" width="1200" height="796" aria-hidden="true">
    <g stroke="var(--dim-line)" stroke-width="1">
      <line x1="521.5" y1="234" x2="521.5" y2="526"/>
      <line x1="208" y1="548.5" x2="500" y2="548.5"/>
      <line x1="940.5" y1="99" x2="940.5" y2="722"/>
      <line x1="912.5" y1="430" x2="912.5" y2="720"/>
    </g>
  </svg>

  <div class="view-label view-label--folded">Folded</div>
  <div class="view-label view-label--open">Open</div>

  <section class="folded-card" aria-label="Card, folded">
    <div class="folded-card__flap"></div>
    <div class="folded-card__mark">
      <div class="brand-name">Stamp,<br>Wrap &amp;<br>Ship</div>
    </div>
  </section>

  <section class="open-card" aria-label="Card, open">
    <div class="open-card__fold open-card__fold--top"></div>
    <div class="open-card__mark">
      <div class="brand-name">Stamp,<br>Wrap &amp;<br>Ship</div>
    </div>
    <div class="open-card__fold open-card__fold--middle"></div>
    <div class="contact">
      <p class="contact__company">Stamp, Wrap &amp; Ship</p>
      <p class="contact__line">Corinne (+61)437182265</p>
      <p class="contact__line">corinne@stampwrapandship.net</p>
      <p class="contact__line contact__web">www.stampwrapandship.net.</p>
    </div>
  </section>

  <span class="dim-label dim-label--vertical dim-label--folded-height">4 cm</span>
  <span class="dim-label dim-label--folded-width">4 cm</span>
  <span class="dim-label dim-label--vertical dim-label--open-height">8.5 cm</span>
  <span class="dim-label dim-label--vertical dim-label--flap-height">4 cm</span>
</body>
</html>
```